Commercial facility maintenance

I need a card design that helps my salesmen make contact with new clients, our product is facility maintenance and heavy industrial maintenance

```html
<!DOCTYPE html>
<html lang="en">
<head>
<meta charset="utf-8">
<title>Halvorsen Millwrights – Business Card</title>
<link href="https://fonts.googleapis.com/css2?family=Bebas+Neue&family=Poppins:ital,wght@0,400;0,500;0,600;0,700;1,400&display=swap" rel="stylesheet">
<style>
  :root{
    --page:#ffffff;
    --card:#242526;
    --card-edge:#2b2c2e;
    --red-fill:#8f1318;
    --red-line:#d9232b;
    --red-bright:#ee2a2f;
    --red-tab:#9e151b;
    --white:#ffffff;
    --photo-a:#e4e4e4;
    --photo-b:#5b6f78;
  }
  *{box-sizing:border-box;margin:0;padding:0}
  html,body{width:923px;height:1200px;overflow:hidden;background:var(--page)}
  body{position:relative;font-family:"Poppins",sans-serif;color:var(--white)}

  .card{
    position:absolute;width:798px;height:456px;
    background:radial-gradient(ellipse at 55% 45%, var(--card-edge) 0%, var(--card) 70%);
    box-shadow:6px 12px 18px rgba(0,0,0,.45);
  }
  .card--front{left:62px;top:97px}
  .card--back{left:61px;top:600px;border-right:3px solid var(--red-line);border-bottom:3px solid var(--red-line)}

  /* front */
  .brand{position:absolute;left:207px;top:131px;display:flex;align-items:center;gap:12px}
  .brand__dot{width:92px;height:92px;border-radius:50%;background:var(--red-fill)}
  .brand__name{font-weight:600;color:var(--white);line-height:1}
  .brand__name span{display:block}
  .brand__line1{font-size:43px;letter-spacing:1px}
  .brand__line2{font-size:17px;letter-spacing:3.2px;margin-top:6px}

  .service{
    position:absolute;left:116px;width:567px;height:55px;
    background:var(--red-fill);border:2px solid var(--red-line);border-radius:28px;
    display:flex;align-items:center;justify-content:center;
    font-weight:600;font-size:21px;letter-spacing:3.4px;text-transform:uppercase;
  }
  .service--one{top:275px}
  .service--two{top:340px}

  /* back */
  .portrait{
    position:absolute;left:43px;top:56px;width:198px;height:198px;border-radius:50%;
    border:2px solid var(--red-line);
    background:linear-gradient(180deg,var(--photo-a) 0%,#cfc9c4 55%,var(--photo-b) 100%);
  }
  .name-pill{
    position:absolute;left:261px;top:86px;width:415px;height:61px;
    background:var(--red-fill);border:2px solid var(--red-line);border-radius:31px;
    display:flex;align-items:center;justify-content:center;
    font-size:31px;letter-spacing:-.3px;text-transform:uppercase;
  }
  .name-pill b{font-weight:700;margin-right:9px}
  .name-pill span{font-weight:400}
  .role{position:absolute;left:263px;top:157px;font-style:italic;font-size:18.5px;line-height:23px}
  .divider{position:absolute;left:261px;top:228px;width:489px;border-top:1.5px dashed var(--red-line)}

  .contact-tab{
    position:absolute;left:0;top:307px;width:135px;height:74px;
    background:var(--red-tab);border:2px solid var(--red-line);border-left:none;border-radius:0 12px 12px 0;
    font-family:"Bebas Neue",sans-serif;font-size:50px;color:var(--red-bright);
    display:flex;align-items:center;justify-content:center;padding-top:4px;letter-spacing:-.5px;
  }
  .contact-item{position:absolute;display:flex;align-items:center;gap:12px;font-size:19.5px;font-weight:400}
  .contact-item svg{width:20px;height:20px;flex:none}
  .contact-item--phone{left:156px;top:307px}
  .contact-item--office{left:155px;top:353px}
  .contact-item--mail{left:364px;top:307px;gap:16px}
  .contact-item--web{left:364px;top:353px;gap:16px}
</style>
</head>
<body>

<section class="card card--front">
  <div class="brand">
    <div class="brand__dot"></div>
    <div class="brand__name">
      <span class="brand__line1">HALVORSEN</span>
      <span class="brand__line2">MILLWRIGHTS LLC.</span>
    </div>
  </div>
  <div class="service service--one">Commercial Facility Maintenance</div>
  <div class="service service--two">Heavy Industrial Maintenance</div>
</section>

<section class="card card--back">
  <div class="portrait" role="img" aria-label="Portrait photo of the sales specialist"></div>
  <div class="name-pill"><b>Daniel</b><span>Marsh</span></div>
  <p class="role">Specialist,<br>Heavy industrial maintenance</p>
  <div class="divider"></div>

  <div class="contact-tab">Contact</div>

  <div class="contact-item contact-item--phone">
    <svg viewBox="0 0 24 24" fill="#e0252b"><path d="M6.6 10.8a15.1 15.1 0 0 0 6.6 6.6l2.2-2.2a1 1 0 0 1 1-.25 11.4 11.4 0 0 0 3.6.57 1 1 0 0 1 1 1V20a1 1 0 0 1-1 1A17 17 0 0 1 3 4a1 1 0 0 1 1-1h3.5a1 1 0 0 1 1 1c0 1.25.2 2.45.57 3.57a1 1 0 0 1-.25 1z"/><path d="M14 3a7 7 0 0 1 7 7h-2a5 5 0 0 0-5-5zm0 3a4 4 0 0 1 4 4h-2a2 2 0 0 0-2-2z"/></svg>
    <span>509-555-0142</span>
  </div>
  <div class="contact-item contact-item--office">
    <svg viewBox="0 0 24 24" fill="#e0252b"><rect x="2" y="4" width="6" height="17" rx="2"/><rect x="9" y="7" width="13" height="14" rx="2"/><rect x="11" y="2" width="3" height="6"/><g fill="#242526"><rect x="12" y="10" width="2" height="2"/><rect x="16" y="10" width="2" height="2"/><rect x="12" y="14" width="2" height="2"/><rect x="16" y="14" width="2" height="2"/><rect x="12" y="17.5" width="2" height="2"/><rect x="16" y="17.5" width="2" height="2"/></g></svg>
    <span>509-555-0187</span>
  </div>
  <div class="contact-item contact-item--mail">
    <svg viewBox="0 0 24 24" fill="#e0252b"><path d="M2 5h20v14H2z"/><path d="M2 5l10 8 10-8" fill="none" stroke="#242526" stroke-width="1.6"/></svg>
    <span>daniel@halvorsenmillwrights.com</span>
  </div>
  <div class="contact-item contact-item--web">
    <svg viewBox="0 0 24 24" fill="none" stroke="#e0252b" stroke-width="2"><circle cx="12" cy="12" r="9.5" fill="#e0252b"/><path d="M2.5 12h19M12 2.5c-3 3-3 16 0 19M12 2.5c3 3 3 16 0 19M4 7h16M4 17h16" stroke="#242526" stroke-width="1.3"/></svg>
    <span>www.halvorsenmillwrights.com</span>
  </div>
</section>

</body>
</html>
```